Brantwell Group needs a business card design

We need a new business card design using the logo recently selected in a logo competition on Pixel Forum. Our business is a consultancy specializing in aviation and energy and the winning business card design will promote an image of precision and professionalism with creativity.

Please use the logo with the name on the front of the card and use a complementary font. Make the back white with either the light grey or dark grey logo.

Target Market(s)

Senior finance and legal leaders at aviation and energy companies

Industry/Entity Type

Management Consulting

Contact Information for Business Card

Peter Haldane
President
Brantwell Group

www.brantwellgroup.example

(555) 304-6198
ph@brantwellgroup.example

Requirements
Must have
• Professional font that goes well with the logo font

```html
<!DOCTYPE html>
<html lang="en">
<head>
<meta charset="utf-8">
<title>Brantwell Group – Business Card</title>
<link rel="stylesheet" href="https://fonts.googleapis.com/css2?family=Roboto:wght@300;400&display=swap">
<style>
  :root {
    --backdrop: #c4c4c4;
    --card: #ffffff;
    --navy: #0e3f73;
    --grey-mark: #646464;
    --ink: #555555;
    --band-text: #dfe6ee;
    --rule: #5b7da3;
  }
  * { box-sizing: border-box; margin: 0; padding: 0; }
  html, body { width: 1200px; height: 800px; overflow: hidden; }
  body {
    background: var(--backdrop);
    font-family: "Roboto", Arial, sans-serif;
    position: relative;
  }
  .card {
    position: absolute;
    width: 525px;
    height: 300px;
    background: var(--card);
    left: 337px;
    overflow: hidden;
    box-shadow: 0 2px 6px rgba(0,0,0,0.12);
  }
  .card--back { top: 70px; display: flex; align-items: center; justify-content: center; }
  .card--front { top: 430px; }

  .back-name {
    display: flex; align-items: center; gap: 18px;
    font-weight: 300; font-size: 40px; letter-spacing: 6px;
    color: var(--grey-mark); text-transform: uppercase;
  }
  .back-name .mark-square { width: 30px; height: 30px; background: var(--grey-mark); }

  .brand {
    position: absolute; left: 30px; top: 78px; width: 170px;
    display: flex; flex-direction: column; align-items: center; gap: 12px;
    color: var(--navy); font-weight: 400; text-transform: uppercase; text-align: center;
  }
  .brand .mark-square { width: 22px; height: 22px; background: var(--navy); }
  .brand .brand-name { font-size: 19px; letter-spacing: 3px; line-height: 1.35; }

  .divider {
    position: absolute; left: 212px; top: 38px; width: 1px; height: 150px;
    background: var(--rule);
  }

  .contact { position: absolute; left: 248px; top: 52px; color: var(--ink); }
  .contact .person { font-size: 22px; font-weight: 400; }
  .contact .role {
    font-size: 11px; letter-spacing: 3px; color: var(--navy);
    text-transform: uppercase; margin-top: 4px;
  }
  .contact .lines { margin-top: 24px; font-size: 14px; line-height: 1.45; }
  .contact .lines dt {
    float: left; width: 16px; font-weight: 400; color: var(--navy); font-size: 13px;
  }
  .contact .lines dd { margin-left: 16px; }

  .band {
    position: absolute; left: 0; right: 0; bottom: 0; height: 92px;
    background: var(--navy); color: var(--band-text);
    display: flex; flex-direction: column; justify-content: center;
    padding-left: 40px;
    font-weight: 300; font-size: 16px; letter-spacing: 4px; line-height: 1.45;
    text-transform: uppercase;
  }
</style>
</head>
<body>
  <section class="card card--back" aria-label="Card back">
    <div class="back-name"><span class="mark-square"></span>Brantwell</div>
  </section>

  <section class="card card--front" aria-label="Card front">
    <div class="brand">
      <span class="mark-square"></span>
      <span class="brand-name">Brantwell<br>Group</span>
    </div>
    <div class="divider"></div>
    <div class="contact">
      <p class="person">Peter J. Haldane</p>
      <p class="role">President</p>
      <dl class="lines">
        <dt>T</dt><dd>(555) 304-6198</dd>
        <dt>E</dt><dd>ph@brantwellgroup.example</dd>
      </dl>
    </div>
    <div class="band">
      <span>Finance and Strategy Consulting</span>
      <span>Aviation - Manufacturing - Energy</span>
    </div>
  </section>
</body>
</html>
```